E-Book-Cover für meinen Roman Was der Nebel trägt
Sehr angenehmer Kontakt, das Beschriebene wurde auf Anhieb in die Richtung umgesetzt, die ich angestrebt habe. Änderungswünsche wurden prompt und unermüdlich umgesetzt, bis das Endergebnis stand. Sehr zu empfehlen!
Zielgruppe
Ich veröffentliche in Eigenregie meinen Roman namens 'Was der Nebel trägt' im Rahmen des Self-Publishing Angebots von Lesowa.de
Bei meinem Werk handelt es sich um Belletristik: eine Geschichte aus dem Leben, die traurige und lustige Elemente zu gleichen Teilen eint. Behandelt wird der Lebensabschnitt eines Jugendlichen, der zu früh Erfahrung mit dem Tod macht, als seine Mutter schwer erkrankt. Gleichzeitig gilt es, den (humorvoll verpackten) Alltag zu meistern, in dem er wieder und wieder auf Ablehnung und Distanz angesichts seiner ungewöhnlichen und misslichen Lage stößt. Es gelingt ihm nicht mehr, Teil seiner gleichaltrigen Mitstreiter zu werden.
Gleichzeitig gibt es einen zweiten Handlungsstrang, in dem eine ebenfalls Jugendliche ähnliche Erfahrungen macht, auch wenn die Umstände andere sind, ebenso wie die Reaktion darauf. Während der männliche Protagonist wiederholt von seinem Umkreis enttäuscht wird, stellt er sich am Ende der Prüfung, der er nicht entkommen kann. Sein weibliches Pendant hingegen tritt eine überstürzte Flucht mit ungewissem Ausgang an. Beide Stränge sind lose miteinander verwoben, und als Leser stellt man sich zusehends die Frage, ob und wann diese verbunden werden. Eine Auflösung erfolgt am Schluss.
Nach einigen Testlesern stellte sich heraus, dass jene am meisten begeistert waren, die selbst ähnliche Erfahrungen gemacht haben, wie die fiktiven Personen. Grundsätzlich lässt sich aber sagen, dass der Schreibstil, die beschriebenen Medien und Situationen eher auf (junge) Erwachsene zugeschnitten sind. Dennoch handelt es sich nicht um ein klassisches Jugendbuch, oft werden Dinge beschrieben, die für Minderjährige nicht geeignet sind. Als (Haupt)zielgruppe würde ich grob den Rahmen 20-40 Jahre vorgeben, wobei die Leser eher noch älter als jünger sein dürfen.
Aufgabenstellung
Zunächst technisch: (Angaben lt. Lesowa)
JPEG oder TIFF-Datei
mindestens 1000 Pixel an der längsten Seite
Idealverhältnis von Bildhöhe- und breite: 1,6 (Beispiel: 1000 x 1600)
bei weißen Covern sollte ein 2-3 Pixel breiter, grauer Rand hinzugefügt werden, damit sich das Cover von der Website selbst abhebt
Weiterhin zu beachten:
-Hauptsächlich wird es auf eBook Readern gelesen, die nur in Graustufen darstellen. Das Cover sollte also in jedem Fall auch in Schwarz-Weiß nichts von seiner Wirkung einbüßen!
Selbiges gilt für eine Miniaturansicht!
Autor: Matthias Krollner
Titel: Was der Nebel trägt
Zusatz: Roman
Nun zu den wichtigsten Vorgaben:
-Selbstverständlich soll das Cover Aufmerksamkeit erzeugen und neugierig machen.
-Das Thema "anders sein" / "im Abseits stehen" / "hin- und hergetrieben werden" muss auf jeden Fall rübergebracht werden, da dies auch das Kernthema des Buches ist.
-Bei der Schriftart gibt es keine bestimmte Vorgabe, nur bitte nichts in Kapitälchen oder Großbuchstaben. (z.B. WAS DER NEBEL TRÄGT)
-Es soll auf keinen Fall übertrieben ernst oder möchtegern-schnulzig rüberkommen. (Bilder vom Strand, untergehender Sonne und weitere Klischees.)
-Vielmehr darf man dem Cover bereits ansehen, dass es ein ernstes Thema auch mit Humor nehmen kann. z.B. durch Stilisierung, einfache Farben anstatt aufwändiger Realaufnahmen und Schatten, evtl. auch in Richtung Comic, aber nicht zu albern.
-Die Platzierung von Autor und Titel darf klassisch sein, gerne aber auch ungewöhnlich überraschend.
Ich habe diesem Inserat einige Entwürfe meinerseits beigefügt, wie ich das o.g. Thema stilisieren würde, z.B.:
der Querschnitt eines einfahrenden Zuges (Hauptverkehrsmittel im Buch), bei dem in allen Fenstern Licht brennt, mit Ausnahme von einem. (Hier dürfen gerne auch die Profile von Menschen hinzug..

```html
<!DOCTYPE html>
<html lang="de">
<head>
<meta charset="utf-8">
<title>Was der Nebel trägt – Matthias Krollner</title>
<link rel="stylesheet" href="https://fonts.googleapis.com/css2?family=Kaushan+Script&display=swap">
<style>
  :root {
    --page: #ffffff;
    --frame: #dcdcdc;
    --sky-coral: #dc5a4b;
    --sky-rose: #e8958a;
    --field-amber: #f5b041;
    --field-red: #dd1a20;
    --ink: #1a1a1a;
    --title-orange: #e4502a;
    --title-red: #e0312f;
    --title-crimson: #b81c28;
    --title-amber: #f0921e;
    --label-grey: #6d6d6d;
    --author: #333333;
  }
  html, body {
    margin: 0;
    padding: 0;
    width: 840px;
    height: 1200px;
    overflow: hidden;
    background: var(--page);
  }
  .canvas {
    position: relative;
    width: 840px;
    height: 1200px;
  }
  .cover {
    display: block;
    width: 840px;
    height: 1200px;
  }
  .cover-frame {
    fill: var(--page);
    stroke: var(--frame);
    stroke-width: 7;
  }
  .lettering {
    font-family: "Kaushan Script", cursive;
  }
  .title-was { fill: var(--title-orange); font-size: 92px; }
  .title-der { fill: var(--title-red); font-size: 62px; }
  .title-nebel { fill: var(--title-crimson); font-size: 118px; }
  .title-traegt { fill: var(--title-amber); font-size: 70px; }
  .genre { fill: var(--label-grey); font-size: 42px; }
  .author { fill: var(--author); font-size: 56px; }
</style>
</head>
<body>
<main class="canvas">
  <svg class="cover" viewBox="0 0 840 1200" xmlns="http://www.w3.org/2000/svg">
    <defs>
      <linearGradient id="railway-tones" x1="0" y1="0" x2="0" y2="1">
        <stop offset="0" stop-color="#ffffff"/>
        <stop offset="0.28" stop-color="#ffffff"/>
        <stop offset="0.38" stop-color="#dc5a4b"/>
        <stop offset="0.62" stop-color="#dc5a4b"/>
        <stop offset="0.70" stop-color="#f5b041"/>
        <stop offset="0.78" stop-color="#dd1a20"/>
        <stop offset="0.90" stop-color="#e8958a"/>
        <stop offset="1" stop-color="#ffffff"/>
      </linearGradient>
    </defs>

    <rect class="cover-frame" x="127" y="131" width="597" height="969"/>

    <rect class="cover-illustration" x="131" y="135" width="589" height="560"
          fill="url(#railway-tones)" role="img"
          aria-label="Stilisierte Pinselzeichnung: Bahngleise mit Oberleitungsmasten führen zum Horizont unter einem korallenroten Himmel, gelbe und rote Felder zu beiden Seiten"/>

    <g class="title lettering">
      <text class="title-was" x="384" y="704">Was</text>
      <text class="title-der" x="244" y="788">der</text>
      <text class="title-nebel" x="334" y="790">Nebel</text>
      <text class="title-traegt" x="430" y="858">trägt</text>
    </g>

    <text class="genre lettering" x="434" y="938">Roman</text>

    <text class="author lettering" x="420" y="1032" text-anchor="middle">Matthias Krollner</text>
  </svg>
</main>
</body>
</html>
```